Making our lobbying activities and sports better visible for members and partners.

We are the Velden Assocation of Leisure Gear Merchant and and Trade. We are doing lobbying and having several special groupings and services. With a better power point we want to show better to the board, the members and partner what we are doing.

```html
<!DOCTYPE html>
<html lang="en">
<head>
<meta charset="utf-8">
<title>VELDA – Corporate Business Slide Presentation</title>
<link href="https://fonts.googleapis.com/css2?family=Roboto:wght@300;400;500;700;900&display=swap" rel="stylesheet">
<style>
:root{
  --navy:#2b2e45;
  --ink:#1f2238;
  --blue:#45a4ef;
  --grey:#eceff1;
  --card-grey:#c9ccd2;
  --muted:#4f5466;
  --page:#ececec;
  --white:#ffffff;
}
*{box-sizing:border-box}
html,body{margin:0;width:1200px;height:1037px;overflow:hidden}
body{background:linear-gradient(180deg,#e6e6e6 0%,#f1f1f1 100%);font-family:'Roboto',sans-serif;position:relative;color:var(--ink)}
.slide{position:absolute;width:280px;height:157px;overflow:hidden;background:var(--white);box-shadow:0 2px 6px rgba(0,0,0,.22)}
.slide--dark{background:var(--navy)}
.slide .bg{position:absolute;left:0;top:0;width:280px;height:157px}
.t{position:absolute;margin:0;line-height:1.15;white-space:nowrap}
.copy{position:absolute;margin:0;font-size:3.6px;line-height:1.55;color:var(--muted);white-space:normal}
.copy--light{color:#e6e8f0}
.accent{color:var(--blue)}
.title{font-weight:700;color:var(--ink);font-size:11px;text-transform:uppercase}
.link{text-decoration:underline;color:var(--ink);font-weight:500}
.brand{position:absolute;display:flex;align-items:center;gap:2px;font-weight:500;font-size:7px;letter-spacing:.3px;color:var(--white)}
.brand__mark{width:4px;height:4px;background:var(--blue)}
.hero{position:absolute;left:300px;top:26px;width:600px;height:336px}
.hero .slide{transform:scale(2.1429);transform-origin:0 0;box-shadow:0 1px 3px rgba(0,0,0,.2)}
.right{text-align:right}
.centered{text-align:center}
.member-name{font-size:4.6px;font-weight:700;color:var(--ink)}
.member-role{font-size:3.3px;font-weight:500;color:var(--blue)}
.service-name{font-size:6.2px;color:var(--ink)}
.stat{font-size:11px;font-weight:500}
.stat-label{font-size:3.8px;color:var(--ink)}
.item-title{font-size:4.4px;font-weight:700;color:var(--ink)}
.card-title{font-size:4.6px;font-weight:700;color:var(--white)}
</style>
</head>
<body>

<!-- Cover, large -->
<div class="hero">
  <section class="slide slide--dark slide--cover">
    <svg class="bg" viewBox="0 0 280 157">
      <polygon points="0,0 122,0 94,78 140,157 0,157" fill="url(#snowA)" role="img" aria-label="Photo of ski tourers climbing a snowy slope"/>
      <polygon points="122,0 148,0 112,78 166,157 140,157 94,78" fill="var(--blue)"/>
      <defs><linearGradient id="snowA" x1="0" y1="0" x2="0" y2="1"><stop offset="0" stop-color="#8d949e"/><stop offset=".6" stop-color="#b9bec5"/><stop offset="1" stop-color="#d9dce0"/></linearGradient></defs>
    </svg>
    <div class="brand" style="right:14px;top:12px"><span class="brand__mark"></span>VELDA</div>
    <p class="t right" style="right:14px;top:44px;font-size:13px;font-weight:300;color:var(--white)">CORPORATE</p>
    <p class="t right" style="right:14px;top:59px;font-size:13px;font-weight:700;color:var(--white)">BUSINESS SLIDE</p>
    <p class="t right" style="right:14px;top:74px;font-size:13px;font-weight:700;color:var(--blue)">PRESENTATION</p>
    <p class="copy copy--light right" style="right:14px;top:97px;width:110px">We represent retailers and makers of leisure gear across the region</p>
  </section>
</div>

<!-- Row 1 -->
<section class="slide slide--dark slide--cover" style="left:11px;top:418px">
  <svg class="bg" viewBox="0 0 280 157">
    <polygon points="0,0 122,0 94,78 140,157 0,157" fill="url(#snowB)" role="img" aria-label="Photo of ski tourers climbing a snowy slope"/>
    <polygon points="122,0 148,0 112,78 166,157 140,157 94,78" fill="var(--blue)"/>
    <defs><linearGradient id="snowB" x1="0" y1="0" x2="0" y2="1"><stop offset="0" stop-color="#8d949e"/><stop offset=".6" stop-color="#b9bec5"/><stop offset="1" stop-color="#d9dce0"/></linearGradient></defs>
  </svg>
  <div class="brand" style="right:14px;top:12px"><span class="brand__mark"></span>VELDA</div>
  <p class="t right" style="right:14px;top:44px;font-size:13px;font-weight:300;color:var(--white)">CORPORATE</p>
  <p class="t right" style="right:14px;top:59px;font-size:13px;font-weight:700;color:var(--white)">BUSINESS SLIDE</p>
  <p class="t right" style="right:14px;top:74px;font-size:13px;font-weight:700;color:var(--blue)">PRESENTATION</p>
  <p class="copy copy--light right" style="right:14px;top:97px;width:110px">We represent retailers and makers of leisure gear across the region</p>
</section>

<section class="slide slide--dark slide--welcome" style="left:311px;top:418px">
  <svg class="bg" viewBox="0 0 280 157">
    <defs><linearGradient id="valley" x1="0" y1="0" x2="0" y2="1"><stop offset="0" stop-color="#9cc0e0"/><stop offset=".35" stop-color="#8b8f86"/><stop offset=".65" stop-color="#4e6b34"/><stop offset="1" stop-color="#3c5030"/></linearGradient></defs>
    <rect x="150" y="0" width="130" height="157" fill="url(#valley)" role="img" aria-label="Photo of a mountain valley with forest and waterfall"/>
    <polygon points="180,40 215,40 232,72 200,112 175,112 200,72" fill="var(--blue)"/>
    <polygon points="0,0 165,0 200,72 160,157 0,157" fill="var(--navy)"/>
    <polygon points="160,157 192,105 214,105 186,157" fill="var(--white)"/>
    <polyline points="16,33 22,41 16,49" fill="none" stroke="var(--blue)" stroke-width="3"/>
  </svg>
  <p class="t" style="left:32px;top:30px;font-size:12px;font-weight:700;color:var(--white)">Welcome to</p>
  <p class="t" style="left:32px;top:44px;font-size:7.5px;font-weight:300;color:var(--white)">Presentation template</p>
  <p class="t" style="left:14px;top:73px;font-size:4.8px;font-weight:700;letter-spacing:.6px;color:var(--white)">COMPANY CEO MESSAGE</p>
  <p class="copy copy--light" style="left:14px;top:82px;width:138px">Our board welcomes you to this overview of our work. We speak for members in policy talks, run special groupings for each trade segment and offer services that help shops and brands grow. This deck shows what we do and why it matters.</p>
</section>

<section class="slide slide--about" style="left:610px;top:418px">
  <svg class="bg" viewBox="0 0 280 157">
    <defs><linearGradient id="forest" x1="0" y1="0" x2="1" y2="1"><stop offset="0" stop-color="#8d9a6a"/><stop offset=".5" stop-color="#c99a4c"/><stop offset="1" stop-color="#6e5a2c"/></linearGradient></defs>
    <polygon points="175,45 200,45 215,82 200,118 175,118 158,82" fill="var(--blue)"/>
    <polygon points="205,0 280,0 280,157 235,157 185,82" fill="url(#forest)" role="img" aria-label="Photo of a woman stretching in a sunny forest"/>
    <polygon points="185,82 235,157 200,157 178,110" fill="var(--navy)"/>
    <polygon points="198,0 208,0 190,44 184,36" fill="var(--navy)"/>
  </svg>
  <p class="t" style="left:15px;top:20px;font-size:10px;font-weight:400">SOME TEXT</p>
  <p class="t" style="left:15px;top:33px;font-size:10px;font-weight:500;color:var(--blue)">ABOUT COMPANY</p>
  <p class="copy" style="left:15px;top:55px;width:128px">Founded by traders for traders, the association gives leisure gear merchants one strong voice. We track new rules, share market data and bring members together at events through the year.</p>
  <p class="copy link" style="left:15px;top:95px;width:128px">Read more about our history, our board and the groups we run for members</p>
</section>

<section class="slide slide--mission" style="left:910px;top:418px">
  <svg class="bg" viewBox="0 0 280 157">
    <polygon points="14,157 14,88 73,55 132,88 132,157" fill="var(--grey)"/>
    <polygon points="148,157 148,88 207,55 266,88 266,157" fill="var(--grey)"/>
    <polygon points="113,84 142,68 171,84 148,94 148,157 137,157 137,94" fill="var(--navy)"/>
    <polygon points="61,53 85,53 97,73 85,93 61,93 49,73" fill="var(--blue)"/>
    <polygon points="195,53 219,53 231,73 219,93 195,93 183,73" fill="var(--blue)"/>
    <path d="M68,65 h10 v4 a5,5 0 0 1 -10,0 z M73,74 v5 M69,80 h8" fill="none" stroke="var(--white)" stroke-width="1"/>
    <circle cx="207" cy="73" r="7" fill="none" stroke="var(--white)" stroke-width="1"/>
    <circle cx="207" cy="73" r="4" fill="none" stroke="var(--white)" stroke-width="1"/>
    <circle cx="207" cy="73" r="1.2" fill="var(--white)"/>
  </svg>
  <p class="t centered" style="left:0;width:280px;top:21px;font-size:9.5px;font-weight:700">ABOUT MISSION <span class="accent">&amp; VALUE</span></p>
  <p class="t centered" style="left:14px;width:118px;top:102px;font-size:6.5px;font-weight:500;color:var(--blue)">ABOUT MISSION</p>
  <p class="copy centered" style="left:20px;width:106px;top:112px">We speak up for fair rules and strong local trade in sports and leisure goods.</p>
  <p class="t centered" style="left:148px;width:118px;top:102px;font-size:6.5px;font-weight:500;color:var(--blue)">ABOUT VALUE</p>
  <p class="copy centered" style="left:154px;width:106px;top:112px">We value openness, teamwork and a clear focus on what members really need.</p>
</section>

<!-- Row 2 -->
<section class="slide slide--teams" style="left:11px;top:600px">
  <svg class="bg" viewBox="0 0 280 157">
    <polygon points="128,0 280,0 280,80 178,80" fill="var(--navy)"/>
    <path d="M160,23 h5 v5 l-3,5 M168,23 h5 v5 l-3,5" fill="none" stroke="var(--blue)" stroke-width="1.2"/>
    <g fill="var(--blue)" role="img" aria-label="Team member portraits">
      <polygon points="18,79 29,59 53,59 64,79 53,99 29,99"/>
      <polygon points="83,79 94,59 118,59 129,79 118,99 94,99"/>
      <polygon points="148,79 159,59 183,59 194,79 183,99 159,99"/>
      <polygon points="213,79 224,59 248,59 259,79 248,99 224,99"/>
    </g>
  </svg>
  <p class="t title" style="left:14px;top:14px;font-weight:500">COMPANY</p>
  <p class="t title" style="left:14px;top:28px;font-weight:500;color:var(--blue)">TEAMS</p>
  <p class="copy copy--light" style="left:180px;top:18px;width:90px">Our teams work for members every day, from policy desks to event planning and data services.</p>
  <p class="t member-name" style="left:18px;top:113px">Your Name Here</p>
  <p class="t member-role" style="left:18px;top:119px">Position here</p>
  <p class="copy" style="left:18px;top:125px;width:52px">Leads talks with partners and keeps members informed.</p>
  <p class="t member-name" style="left:83px;top:113px">Your Name Here</p>
  <p class="t member-role" style="left:83px;top:119px">Position here</p>
  <p class="copy" style="left:83px;top:125px;width:52px">Runs member events and keeps groupings well organised.</p>
  <p class="t member-name" style="left:148px;top:113px">Your Name Here</p>
  <p class="t member-role" style="left:148px;top:119px">Position here</p>
  <p class="copy" style="left:148px;top:125px;width:52px">Collects market data and prepares reports for our board.</p>
  <p class="t member-name" style="left:213px;top:113px">Your Name Here</p>
  <p class="t member-role" style="left:213px;top:119px">Position here</p>
  <p class="copy" style="left:213px;top:125px;width:52px">Handles press work and shares our news with partners.</p>
</section>

<section class="slide slide--services" style="left:311px;top:600px">
  <svg class="bg" viewBox="0 0 280 157">
    <polygon points="238,0 280,0 258,62 218,62" fill="var(--blue)"/>
    <polygon points="252,62 275,62 265,82" fill="var(--navy)"/>
    <g>
      <polygon points="24,73 36,73 42,84 36,95 24,95 18,84" fill="var(--blue)"/>
      <polygon points="90,73 102,73 108,84 102,95 90,95 84,84" fill="var(--navy)"/>
      <polygon points="156,73 168,73 174,84 168,95 156,95 150,84" fill="var(--blue)"/>
      <polygon points="220,73 232,73 238,84 232,95 220,95 214,84" fill="var(--navy)"/>
    </g>
    <g fill="none" stroke="var(--white)" stroke-width=".8">
      <circle cx="30" cy="82" r="3"/><path d="M28.5,86 h3 M28.5,88 h3"/>
      <circle cx="96" cy="82" r="3"/><path d="M94.5,86 h3 M94.5,88 h3"/>
      <circle cx="162" cy="82" r="3"/><path d="M160.5,86 h3 M160.5,88 h3"/>
      <circle cx="226" cy="82" r="3"/><path d="M224.5,86 h3 M224.5,88 h3"/>
    </g>
  </svg>
  <p class="t" style="left:15px;top:18px;font-size:12px;font-weight:700">COMPANY <span class="accent">SERVICES</span></p>
  <p class="t service-name" style="left:14px;top:108px">Service Name</p>
  <p class="copy" style="left:14px;top:118px;width:52px">Short note on what this service offers members.</p>
  <p class="t service-name" style="left:80px;top:108px">Service Name</p>
  <p class="copy" style="left:80px;top:118px;width:52px">Short note on what this service offers members.</p>
  <p class="t service-name" style="left:146px;top:108px">Service Name</p>
  <p class="copy" style="left:146px;top:118px;width:52px">Short note on what this service offers members.</p>
  <p class="t service-name" style="left:210px;top:108px">Service Name</p>
  <p class="copy" style="left:210px;top:118px;width:52px">Short note on what this service offers members.</p>
</section>

<section class="slide slide--ideas" style="left:610px;top:600px">
  <svg class="bg" viewBox="0 0 280 157">
    <defs><linearGradient id="coast" x1="0" y1="0" x2="0" y2="1"><stop offset="0" stop-color="#dde3ea"/><stop offset=".6" stop-color="#eef1f4"/><stop offset="1" stop-color="#5c5a55"/></linearGradient></defs>
    <polygon points="150,0 280,0 280,140 222,140" fill="url(#coast)" role="img" aria-label="Photo of a woman celebrating on a rocky shore"/>
    <polygon points="222,140 280,140 280,157 212,157" fill="var(--blue)"/>
  </svg>
  <p class="t" style="left:15px;top:20px;font-size:9.5px;font-weight:500">IT’S NOT IDEAS,</p>
  <p class="t" style="left:15px;top:32px;font-size:9.5px;font-weight:500">IT’S ABOUT <span class="accent">MAKING</span></p>
  <p class="t" style="left:15px;top:44px;font-size:9.5px;font-weight:500;color:var(--blue)">IDEAS HAPPEN !</p>
  <p class="copy" style="left:15px;top:66px;width:150px">Good plans need action. Our lobbying turns member ideas into clear proposals, and our groups test them in real shops before we bring them to decision makers.</p>
  <p class="t stat" style="left:23px;top:114px">22.2k</p>
  <p class="t stat-label" style="left:15px;top:130px">Business development</p>
  <p class="t stat" style="left:102px;top:114px;color:var(--blue)">10.1k</p>
  <p class="t stat-label" style="left:95px;top:130px">Business development</p>
</section>

<section class="slide slide--door" style="left:910px;top:600px">
  <svg class="bg" viewBox="0 0 280 157">
    <polygon points="0,0 40,0 0,110" fill="var(--blue)"/>
    <polygon points="40,0 102,0 27,157 0,157 0,110" fill="var(--navy)"/>
    <polygon points="70,55 135,157 30,157" fill="var(--blue)"/>
  </svg>
  <p class="t right" style="right:15px;top:22px;font-size:10px;font-weight:500">IF OPPORTUNITY DOESN’T</p>
  <p class="t right" style="right:15px;top:35px;font-size:10px;font-weight:500;color:var(--blue)">WORK, BUILD A DOOR</p>
  <p class="copy right" style="right:15px;top:60px;width:150px">When doors stay closed, we build new ones. Together with members and partners we open talks, shape fair rules and create room for growth in the leisure gear trade.</p>
  <p class="copy link right" style="right:15px;top:114px;width:100px">Join a grouping and help shape the next steps for our whole trade sector</p>
</section>

<!-- Row 3 -->
<section class="slide slide--chart" style="left:11px;top:773px">
  <svg class="bg" viewBox="0 0 280 157">
    <g font-family="Roboto, sans-serif" font-size="3.6" fill="var(--ink)" text-anchor="end">
      <text x="151" y="31">100</text><text x="151" y="51">80</text><text x="151" y="71">60</text><text x="151" y="91">40</text><text x="151" y="111">20</text>
    </g>
    <line x1="156" y1="28" x2="156" y2="130" stroke="#c8ccd3" stroke-width=".4"/>
    <g>
      <rect x="168" y="50" width="4" height="80" fill="var(--navy)"/><rect x="172" y="50" width="4" height="80" fill="var(--blue)"/>
      <rect x="189" y="40" width="4" height="90" fill="var(--navy)"/><rect x="193" y="40" width="4" height="90" fill="var(--blue)"/>
      <rect x="210" y="68" width="4" height="62" fill="var(--navy)"/><rect x="214" y="68" width="4" height="62" fill="var(--blue)"/>
      <rect x="231" y="52" width="4" height="78" fill="var(--navy)"/><rect x="235" y="52" width="4" height="78" fill="var(--blue)"/>
      <rect x="252" y="25" width="4" height="105" fill="var(--navy)"/><rect x="256" y="25" width="4" height="105" fill="var(--blue)"/>
    </g>
    <g font-family="Roboto, sans-serif" font-size="4.6" fill="var(--ink)" text-anchor="middle">
      <text x="172" y="139">01</text><text x="193" y="139">02</text><text x="214" y="139">03</text><text x="235" y="139">04</text><text x="256" y="139">05</text>
    </g>
    <path d="M18,98 h10 l3,3.5 l-8,8 l-8,-8 z M15,101.5 h16" fill="none" stroke="var(--blue)" stroke-width=".8"/>
  </svg>
  <p class="t" style="left:14px;top:20px;font-size:11px;font-weight:700">BUSINESS <span class="accent">CHART</span></p>
  <p class="copy" style="left:14px;top:42px;width:115px">Member numbers and event reach grew steadily over five years, with the strongest rise in the latest season thanks to new services.</p>
  <p class="t item-title" style="left:36px;top:96px">Business Headline Goes Here</p>
  <p class="copy" style="left:36px;top:104px;width:96px">Sales data shared by members helps us argue for fair terms in policy talks.</p>
</section>

<section class="slide slide--process" style="left:311px;top:773px">
  <svg class="bg" viewBox="0 0 280 157">
    <rect x="15" y="60" width="228" height="20" fill="var(--grey)"/>
    <polygon points="240,45 268,70 240,95" fill="var(--grey)"/>
    <path d="M20,58 h60 v62 a16,16 0 0 1 -16,16 h-44 z" fill="var(--navy)"/>
    <path d="M96,58 h60 v62 a16,16 0 0 1 -16,16 h-44 z" fill="var(--card-grey)"/>
    <path d="M172,58 h60 v62 a16,16 0 0 1 -16,16 h-44 z" fill="var(--blue)"/>
    <g fill="none" stroke="var(--white)" stroke-width=".8">
      <circle cx="50" cy="72" r="3.5"/><path d="M48,77 h4"/>
      <ellipse cx="126" cy="70" rx="4" ry="1.5"/><path d="M122,70 v5 a4,1.5 0 0 0 8,0 v-5"/>
      <rect x="198" y="67" width="8" height="9"/><path d="M200,70 h4 M200,73 h4"/>
    </g>
  </svg>
  <p class="t" style="left:14px;top:20px;font-size:10.5px;font-weight:500">BUSINESS <span class="accent">INFOGRAPHIC</span> SLIDE</p>
  <p class="t card-title centered" style="left:20px;width:60px;top:90px">Business Titile</p>
  <p class="copy copy--light centered" style="left:24px;width:52px;top:98px">Short summary of this step in our member process.</p>
  <p class="t card-title centered" style="left:96px;width:60px;top:90px">Business Titile</p>
  <p class="copy copy--light centered" style="left:100px;width:52px;top:98px">Short summary of this step in our member process.</p>
  <p class="t card-title centered" style="left:172px;width:60px;top:90px">Business Titile</p>
  <p class="copy copy--light centered" style="left:176px;width:52px;top:98px">Short summary of this step in our member process.</p>
</section>

<section class="slide slide--cycle" style="left:610px;top:773px">
  <svg class="bg" viewBox="0 0 280 157">
    <polygon points="104,95 123,62 161,62 180,95 161,128 123,128" fill="none" stroke="var(--navy)" stroke-width="9"/>
    <g fill="var(--blue)" stroke="var(--white)" stroke-width="1">
      <polygon points="118,55 128,55 133,63 128,71 118,71 113,63"/>
      <polygon points="156,55 166,55 171,63 166,71 156,71 151,63"/>
      <polygon points="175,87 185,87 190,95 185,103 175,103 170,95"/>
      <polygon points="156,119 166,119 171,127 166,135 156,135 151,127"/>
      <polygon points="118,119 128,119 133,127 128,135 118,135 113,127"/>
      <polygon points="99,87 109,87 114,95 109,103 99,103 94,95"/>
    </g>
  </svg>
  <p class="t centered" style="left:0;width:280px;top:16px;font-size:10.5px;font-weight:700">BUSINESS INFOGRAPHIC SLIDE</p>
  <p class="t item-title" style="left:18px;top:52px">01 Business Titile here</p>
  <p class="copy" style="left:18px;top:58px;width:52px">Short note on this topic for members.</p>
  <p class="t item-title" style="left:18px;top:85px">02 Business Titile here</p>
  <p class="copy" style="left:18px;top:91px;width:52px">Short note on this topic for members.</p>
  <p class="t item-title" style="left:18px;top:118px">03 Business Titile here</p>
  <p class="copy" style="left:18px;top:124px;width:52px">Short note on this topic for members.</p>
  <p class="t item-title" style="left:212px;top:52px">04 Business Titile here</p>
  <p class="copy" style="left:212px;top:58px;width:52px">Short note on this topic for members.</p>
  <p class="t item-title" style="left:212px;top:85px">05 Business Titile here</p>
  <p class="copy" style="left:212px;top:91px;width:52px">Short note on this topic for members.</p>
  <p class="t item-title" style="left:212px;top:118px">06 Business Titile here</p>
  <p class="copy" style="left:212px;top:124px;width:52px">Short note on this topic for members.</p>
</section>

<section class="slide slide--thanks" style="left:910px;top:773px">
  <svg class="bg" viewBox="0 0 280 157">
    <defs><linearGradient id="summit" x1="0" y1="0" x2="0" y2="1"><stop offset="0" stop-color="#4f8fd0"/><stop offset=".5" stop-color="#a9c6e3"/><stop offset=".7" stop-color="#8a7f55"/><stop offset="1" stop-color="#5f5a3e"/></linearGradient></defs>
    <polygon points="0,0 138,0 60,157 0,157" fill="var(--navy)"/>
    <polygon points="40,28 135,28 160,88 135,150 40,150 15,88" fill="var(--blue)"/>
    <polygon points="30,32 125,32 150,88 125,145 30,145 5,88" fill="url(#summit)" role="img" aria-label="Photo of two hikers on a mountain ridge"/>
    <circle cx="200" cy="135" r="2" fill="var(--blue)"/>
    <circle cx="264" cy="135" r="2" fill="var(--blue)"/>
  </svg>
  <div class="brand" style="right:14px;top:18px;color:var(--ink);font-size:9px"><span class="brand__mark" style="width:5px;height:5px"></span>VELDA</div>
  <p class="t right" style="right:14px;top:52px;font-size:12px;font-weight:700">THANK FOR</p>
  <p class="t right" style="right:14px;top:65px;font-size:15px;font-weight:700;color:var(--blue)">WATCHING</p>
  <p class="copy right" style="right:14px;top:95px;width:118px">Thank you for your time. Contact our office to learn more about membership and services.</p>
  <p class="copy right" style="right:84px;top:131px;width:60px;font-size:3px;line-height:1.3;color:var(--ink)">Company Address Goes here<br>or your location goes here</p>
  <p class="copy right" style="right:20px;top:131px;width:60px;font-size:3px;line-height:1.3;color:var(--ink)">your sample site name here<br>company mail name here</p>
</section>

</body>
</html>
```